Advertisement flyer for fire sprinkler repair parts. The projected audience are contractors.

I need a flyer advertising specific parts that we are stocking at our company "Meridian Valvecraft Supply." I have attached a picture of our logo. I want the title to say "Fire Pump Repair Parts and Accessories." I want to specifically advertise the following parts: Repack Kits and Repair Parts, Jockey Pumps, Pump Controllers, Casing Relief Valves, Air Release Valves, Suction/Discharge Gauges, Pump Shaft Couplers & Shim Kits, Fire Pump Relief Valves, and QN Listed Pressure Reducing Valves. I have attached pictures of the manufacturers I want to advertise on this flyer. I have also attached pictures of some of the parts we are stocking that I would like to be included somewhere in the flyer. I would like all of the pictures to have a transparent background. Also I would like our phone number :(800)-431-2867, and our website www.tolvenspares.example included. I made my own design that I have Attached. You do not have to go based off this design, but I would like the basic content to be the same. We do have Same- Day shipping as well as Free Tech Support if you can include that anywhere.

```html
<!DOCTYPE html>
<html lang="en">
<head>
<meta charset="utf-8">
<title>Fire Pump Repair Parts &amp; Accessories</title>
<link href="https://fonts.googleapis.com/css2?family=Archivo:wght@400;600;700;800&display=swap" rel="stylesheet">
<style>
  :root{
    --navy:#16235c;
    --blue:#2b3f8f;
    --red:#d8202a;
    --steel-1:#b9bcc0;
    --white:#ffffff;
  }
  *{box-sizing:border-box;margin:0;padding:0}
  html,body{width:870px;height:1200px;overflow:hidden}
  body{
    font-family:"Archivo",Arial,sans-serif;
    background:repeating-linear-gradient(180deg,var(--steel-1) 0 2px,#aeb2b6 2px 3px,#c3c6ca 3px 5px);
    position:relative;
  }
  .flyer{
    position:absolute;left:60px;top:42px;width:750px;height:1116px;
    background:var(--white);overflow:hidden;
    box-shadow:0 4px 14px rgba(0,0,0,.35);
  }
  .hero-photo{
    position:absolute;left:0;top:0;width:750px;height:440px;
    background:linear-gradient(160deg,#6b6f75 0%,#a23a36 30%,#c8302c 50%,#7a7d82 75%,#4a4e55 100%);
  }
  .band{position:absolute;left:0;top:0;width:750px;height:1116px}
  .title{
    position:absolute;right:22px;top:44px;width:380px;text-align:right;
    color:var(--white);font-weight:800;font-size:48px;line-height:1.12;
    text-shadow:0 3px 6px rgba(0,0,0,.55);
  }
  .detail-photo{
    position:absolute;border-radius:50%;border:5px solid var(--white);
    box-shadow:0 3px 10px rgba(0,0,0,.4);
  }
  .detail-photo.valve{left:70px;top:300px;width:135px;height:135px;
    background:radial-gradient(circle at 45% 40%,#d9c7a3,#9c8463 60%,#e9e9e9 100%)}
  .detail-photo.kit{left:200px;top:275px;width:145px;height:145px;
    background:radial-gradient(circle at 50% 50%,#6d6f73,#c9cbcf 55%,#f0f0f0 100%)}
  .parts-list{
    position:absolute;right:30px;top:425px;width:340px;list-style:none;
    color:var(--white);font-size:16px;font-weight:600;text-align:right;
  }
  .parts-list li{height:30px;display:flex;justify-content:flex-end;align-items:center;gap:12px;white-space:nowrap}
  .parts-list li::after{content:"";width:0;height:0;border-top:5px solid transparent;
    border-bottom:5px solid transparent;border-right:8px solid var(--red)}
  .product-photo{position:absolute;border-radius:6px}
  .product-photo.pump{left:34px;top:470px;width:260px;height:160px;
    background:linear-gradient(180deg,#d62a2a,#8d1414)}
  .product-photo.prv{left:34px;top:665px;width:80px;height:160px;
    background:linear-gradient(180deg,#c89a55,#8a6630)}
  .product-photo.jockey{left:130px;top:645px;width:70px;height:180px;
    background:linear-gradient(180deg,#e9e9ea,#8d9094)}
  .product-photo.relief{left:215px;top:650px;width:85px;height:175px;
    background:linear-gradient(180deg,#d3262a,#7c1012)}
  .maker-grid{
    position:absolute;left:405px;top:800px;width:320px;
    display:grid;grid-template-columns:1fr 1fr;gap:8px 14px;
  }
  .maker{
    height:44px;display:flex;align-items:center;justify-content:center;
    font-weight:700;font-size:18px;color:var(--navy);white-space:nowrap;
  }
  .maker.red{color:var(--red)}
  .company{
    position:absolute;left:34px;top:855px;width:350px;display:flex;align-items:center;gap:10px;
  }
  .company-mark{width:30px;height:30px;background:var(--red);flex:none}
  .company-name{font-size:24px;font-weight:700;color:var(--navy);line-height:1.05}
  .company-name small{display:block;font-size:16px}
  .footer{
    position:absolute;left:0;top:1020px;width:750px;height:96px;background:var(--navy);
    padding:20px 30px;color:var(--white);
  }
  .footer p{position:relative}
  .call{font-size:21px;font-weight:600}
  .call strong{font-size:26px;font-weight:800}
  .web{font-size:15px;margin-top:4px}
  .footer-stripe{position:absolute;right:0;top:0;width:200px;height:96px;
    background:linear-gradient(100deg,transparent 0 20%,var(--red) 20% 100%)}
</style>
</head>
<body>
<main class="flyer">
  <div class="hero-photo" role="img" aria-label="Photo of a red fire pump room with piping and a pump assembly"></div>

  <svg class="band" viewBox="0 0 750 1116" aria-hidden="true">
    <polygon points="0,440 750,320 750,770 390,770 330,450 0,500" fill="var(--navy)"/>
    <polygon points="0,428 750,308 750,332 0,452" fill="var(--red)"/>
  </svg>

  <h1 class="title">Fire Pump<br>Repair<br>Parts &amp;<br>Accessories!</h1>

  <div class="detail-photo valve" role="img" aria-label="Brass check valve"></div>
  <div class="detail-photo kit" role="img" aria-label="Fire pump repack kit parts"></div>

  <ul class="parts-list">
    <li>Fire Pump Repack Kits</li>
    <li>Jockey Pumps</li>
    <li>Pump Controllers</li>
    <li>Casing Relief Valves</li>
    <li>Air Release Valves</li>
    <li>Suction / Discharge Gauges</li>
    <li>Flow Meters</li>
    <li>Pump Shaft Couplers &amp; Shim Kits</li>
    <li>Fire Pump Relief Valves</li>
    <li>QN Listed Pressure Reducing Valves</li>
  </ul>

  <div class="product-photo pump" role="img" aria-label="Red split-case fire pump"></div>
  <div class="product-photo prv" role="img" aria-label="Bronze pressure reducing valve"></div>
  <div class="product-photo jockey" role="img" aria-label="Vertical stainless jockey pump"></div>
  <div class="product-photo relief" role="img" aria-label="Red fire pump relief valve"></div>

  <div class="maker-grid">
    <div class="maker">Holtby</div>
    <div class="maker">Corvane</div>
    <div class="maker">Ardenflo</div>
    <div class="maker red">Bellmar Pump</div>
    <div class="maker">Stellan</div>
    <div class="maker">Ellison Drake</div>
    <div class="maker red">Quarry Pump</div>
    <div class="maker">Norvik</div>
  </div>

  <div class="company">
    <span class="company-mark"></span>
    <span class="company-name">Meridian Valvecraft<small>Supply Company</small></span>
  </div>

  <footer class="footer">
    <div class="footer-stripe"></div>
    <p class="call">Call Us Today: <strong>(800)-431-2867</strong></p>
    <p class="web">www.tolvenspares.example</p>
  </footer>
</main>
</body>
</html>
```